Granite, Brass and Shingle Roofing LLC needs a new business card

I need a new business card because I have a new address.
I do slate copper and tile roofs. My webpage is: www.granitebrassandshingleroofing.com

```html
<!DOCTYPE html>
<html lang="en">
<head>
<meta charset="utf-8">
<title>Granite, Brass and Shingle Roofing LLC – Business Card</title>
<link href="https://fonts.googleapis.com/css2?family=Poppins:wght@400;500;600&family=Playfair+Display:wght@400&display=swap" rel="stylesheet">
<style>
  :root {
    --stage: #2b2b2d;
    --card-black: #101011;
    --sky: #4f9ccf;
    --sky-light: #7fb7de;
    --paper: #ffffff;
    --ink: #0c0c0c;
    --badge-green: #3aa841;
    --badge-blue: #1d4f9c;
    --badge-grey: #8b8b8b;
  }
  * { margin: 0; padding: 0; box-sizing: border-box; }
  html, body { width: 1200px; height: 900px; overflow: hidden; }
  body { background: var(--stage); position: relative; font-family: "Poppins", sans-serif; }

  .card { position: absolute; width: 640px; height: 366px; overflow: hidden; box-shadow: 0 14px 30px rgba(0,0,0,.45); }

  /* Back of card */
  .card--back { left: 60px; top: 50px; background: var(--card-black); }
  .back-brand { position: absolute; left: 0; right: 0; top: 120px; text-align: center; color: var(--sky); font-family: "Playfair Display", serif; font-weight: 400; }
  .back-brand__mark { display: inline-block; width: 14px; height: 14px; background: var(--sky); margin-right: 10px; vertical-align: middle; }
  .back-brand__name { font-size: 30px; line-height: 1.25; vertical-align: middle; }
  .back-web { position: absolute; left: 0; right: 0; bottom: 48px; text-align: center; color: var(--sky); font-family: "Playfair Display", serif; font-size: 15px; letter-spacing: .5px; }

  /* Front of card */
  .card--front { left: 500px; top: 484px; background: var(--sky); }
  .card__shapes { position: absolute; inset: 0; }
  .front-brand { position: absolute; left: 34px; top: 52px; width: 280px; color: var(--ink); font-family: "Playfair Display", serif; font-weight: 400; font-size: 25px; line-height: 1.2; display: flex; align-items: flex-start; gap: 10px; }
  .front-brand__mark { flex: none; width: 12px; height: 12px; background: var(--ink); margin-top: 9px; }

  .contact { position: absolute; right: 26px; top: 116px; list-style: none; text-align: right; color: var(--paper); font-size: 13.5px; line-height: 1.45; }
  .contact li { display: flex; justify-content: flex-end; align-items: center; gap: 8px; }
  .contact svg { width: 12px; height: 12px; flex: none; }

  .person { position: absolute; left: 34px; top: 198px; color: var(--paper); }
  .person__name { font-weight: 600; font-size: 20px; letter-spacing: .5px; }
  .person__role { font-weight: 400; font-size: 16px; letter-spacing: .5px; margin-top: -2px; }

  .address { position: absolute; left: 34px; top: 266px; color: var(--ink); font-size: 16px; line-height: 1.45; font-weight: 500; }

  .badge { position: absolute; }
  .badge--membrane { left: 430px; top: 226px; width: 120px; height: 34px; border-radius: 4px; background: var(--badge-blue); }
  .badge--membrane::before { content: ""; position: absolute; left: -40px; top: 2px; width: 30px; height: 30px; background: var(--badge-green); border-radius: 3px; }
  .badge--tile { left: 572px; top: 214px; width: 50px; height: 50px; border-radius: 50%; border: 4px solid var(--badge-grey); }
</style>
</head>
<body>

  <section class="card card--back" aria-label="Back of business card">
    <div class="back-brand">
      <span class="back-brand__mark"></span><span class="back-brand__name">Granite, Brass &amp; Shingle<br>Roofing</span>
    </div>
    <p class="back-web">www.granitebrassandshingleroofing.com</p>
  </section>

  <section class="card card--front" aria-label="Front of business card">
    <svg class="card__shapes" viewBox="0 0 640 366" preserveAspectRatio="none" aria-hidden="true">
      <line x1="0" y1="188" x2="330" y2="188" stroke="var(--sky-light)" stroke-width="1"/>
      <line x1="318" y1="104" x2="640" y2="104" stroke="var(--paper)" stroke-width="3"/>
      <polygon points="0,252 340,252 356,198 640,198 640,292 398,292 385,340 0,340" fill="var(--paper)"/>
      <polygon points="0,340 385,340 376,366 0,366" fill="var(--ink)"/>
    </svg>

    <div class="front-brand"><span class="front-brand__mark"></span><span>Granite, Brass &amp; Shingle Roofing</span></div>

    <ul class="contact">
      <li>(440)555-0187
        <svg viewBox="0 0 24 24" aria-hidden="true"><path fill="#fff" d="M6.6 10.8a15 15 0 0 0 6.6 6.6l2.2-2.2c.3-.3.7-.4 1-.2 1.1.4 2.3.6 3.6.6.6 0 1 .4 1 1V20c0 .6-.4 1-1 1C10.6 21 3 13.4 3 4c0-.6.4-1 1-1h3.5c.6 0 1 .4 1 1 0 1.3.2 2.5.6 3.6.1.3 0 .7-.2 1z"/></svg>
      </li>
      <li>gbsroofingllc@mailbox.com
        <svg viewBox="0 0 24 24" aria-hidden="true"><rect x="2" y="5" width="20" height="14" rx="2" fill="none" stroke="#fff" stroke-width="2"/><path d="M3 6l9 7 9-7" fill="none" stroke="#fff" stroke-width="2"/></svg>
      </li>
      <li>www.granitebrassandshingleroofing.com
        <svg viewBox="0 0 24 24" aria-hidden="true"><circle cx="12" cy="12" r="9" fill="none" stroke="#fff" stroke-width="2"/><path d="M3 12h18M12 3c3 3 3 15 0 18M12 3c-3 3-3 15 0 18" fill="none" stroke="#fff" stroke-width="1.6"/></svg>
      </li>
    </ul>

    <div class="person">
      <p class="person__name">MARTON (MATT) HALE</p>
      <p class="person__role">OWNER</p>
    </div>

    <address class="address" style="font-style:normal">2870 Linden Rd<br>Ashford, OH 44000</address>

    <span class="badge badge--membrane" role="img" aria-label="Roofing membrane certification badge"></span>
    <span class="badge badge--tile" role="img" aria-label="Authorized tile roofer badge"></span>
  </section>

</body>
</html>
```